Finiding oppertunites in Real Estate 6.15.20

size of ad 7” x 9.6”
1-I like the ad to stand out and attract people's attention.
2-you should be able to see the text of the ad clearly .. see the attachment anything in yellow is instructions.
3-the list of topics should not be the main part of the ad
4-if you decide you want a picture or vector of a person .. (you decide)
then it should be a white male about 25-30 years old wearing a solid white or blue shirt and not long hair.
5-leave 1 inch for footer
see attachment
Good luck

Target Market(s)

potential male students 25-35 years of age

Industry/Entity Type

Education

Requirements
Must have
• will stand out and people would want to see it.
should be able to read the words of ad
Nice to have
• how to make money in real estate on one line

```html
<!DOCTYPE html>
<html lang="en">
<head>
<meta charset="utf-8">
<title>Real Estate Career Course</title>
<link href="https://fonts.googleapis.com/css2?family=Oswald:wght@600;700&family=Roboto:wght@400;500;900&display=swap" rel="stylesheet">
<style>
  :root{
    --page:#e4e4e4;
    --paper:#ffffff;
    --orange:#e68a2e;
    --sand:#ecebe6;
    --ink:#111111;
    --text:#1f1f1f;
    --white:#ffffff;
    --red-light:#f08a8e;
    --red:#d11a22;
    --red-deep:#8e0d12;
  }
  *{margin:0;padding:0;box-sizing:border-box}
  html,body{width:1200px;height:1200px;overflow:hidden;background:var(--page)}
  body{position:relative;font-family:'Roboto',sans-serif}
  .ad{position:absolute;left:0;top:162px;width:1200px;height:875px;background:var(--paper);overflow:hidden}
  .hero-photo{position:absolute;left:0;top:0;width:1200px;height:406px;
    background:linear-gradient(180deg,#7fb3e0 0%,#cfe2f2 28%,#efe2cf 52%,#d9a86a 72%,#6f9a5a 100%)}
  .info-band{position:absolute;left:0;top:406px;width:1200px;height:184px;background:var(--orange)}
  .headline{position:absolute;left:26px;top:412px;font-weight:900;font-size:53px;letter-spacing:-0.5px;color:var(--ink);white-space:nowrap;line-height:1.1}
  .selling-points{position:absolute;left:35px;top:482px;list-style:none;color:var(--white);font-size:22px;line-height:32.5px}
  .selling-points li{position:relative;padding-left:17px;white-space:nowrap}
  .selling-points li::before{content:"";position:absolute;left:0;top:12px;width:9px;height:9px;background:var(--white)}
  .topics{position:absolute;left:0;top:590px;width:1200px;height:162px;background:var(--sand)}
  .topics-title{position:absolute;left:406px;top:8px;transform:translateX(-50%);font-weight:500;font-size:19px;color:var(--ink)}
  .topic-col{position:absolute;top:38px;list-style:none;font-size:18px;color:var(--text);line-height:26.2px}
  .topic-col li{display:flex;align-items:center;gap:7px;white-space:nowrap}
  .tick{width:14px;height:14px;flex:none}
  .col-1{left:29px}.col-2{left:247px}.col-3{left:476px}.col-4{left:657px}
  .presenter-photo{position:absolute;left:791px;top:176px;width:409px;height:573px;
    background:linear-gradient(180deg,rgba(60,45,40,.0) 0%,#2a2a2c 40%,#1b1b1d 100%);
    border-radius:160px 160px 0 0}
  .footer-space{position:absolute;left:0;top:752px;width:1200px;height:123px;background:var(--paper)}
  .promo-burst{position:absolute;left:21px;top:137px;width:280px;height:280px}
  .promo-text{position:absolute;left:61px;width:200px;text-align:center;font-family:'Oswald',sans-serif;color:var(--white);line-height:1;text-shadow:0 1px 2px rgba(0,0,0,.45)}
  .promo-title{top:198px;font-weight:700;font-size:40px;letter-spacing:-0.5px;line-height:39px}
  .promo-rule{position:absolute;left:77px;width:167px;height:1.5px;background:var(--white)}
  .promo-course{top:285px;font-weight:600;font-size:21px}
  .promo-start{top:313px;font-weight:600;font-size:15px}
  .promo-date{top:329px;font-weight:700;font-size:30px}
</style>
</head>
<body>
<main class="ad">
  <div class="hero-photo" role="img" aria-label="Photo of a modern luxury villa with a pool, palm trees and blue sky"></div>
  <section class="info-band">
  </section>
  <h1 class="headline">REAL ESTATE CAREER COURSE</h1>
  <ul class="selling-points">
    <li>How to make money in Real Estate?</li>
    <li>For those who have started or would like to go into Real Estate</li>
    <li>An Investment in knowledge opens up untold opportunities</li>
  </ul>
  <section class="topics">
    <h2 class="topics-title">Topics</h2>
    <svg width="0" height="0" style="position:absolute">
      <symbol id="tick" viewBox="0 0 14 14"><circle cx="7" cy="7" r="7" fill="#e68a2e"/><path d="M3.8 7.2l2.2 2.1 4.2-4.4" fill="none" stroke="#fff" stroke-width="1.8" stroke-linecap="round" stroke-linejoin="round"/></symbol>
    </svg>
    <ul class="topic-col col-1">
      <li><svg class="tick"><use href="#tick"/></svg>Single Family</li>
      <li><svg class="tick"><use href="#tick"/></svg>Multifamily</li>
      <li><svg class="tick"><use href="#tick"/></svg>Management</li>
      <li><svg class="tick"><use href="#tick"/></svg>Real Estate Concepts</li>
    </ul>
    <ul class="topic-col col-2">
      <li><svg class="tick"><use href="#tick"/></svg>Real Estate Law</li>
      <li><svg class="tick"><use href="#tick"/></svg>Investment Properties</li>
      <li><svg class="tick"><use href="#tick"/></svg>Foreclousure</li>
      <li><svg class="tick"><use href="#tick"/></svg>Rehab</li>
    </ul>
    <ul class="topic-col col-3">
      <li><svg class="tick"><use href="#tick"/></svg>Short Sales</li>
      <li><svg class="tick"><use href="#tick"/></svg>Development</li>
      <li><svg class="tick"><use href="#tick"/></svg>Financial Modeling</li>
      <li><svg class="tick"><use href="#tick"/></svg>HUD Properties</li>
    </ul>
    <ul class="topic-col col-4">
      <li><svg class="tick"><use href="#tick"/></svg>Due Diligence</li>
    </ul>
  </section>
  <div class="presenter-photo" role="img" aria-label="Photo of a young businessman in a dark suit, blue shirt and red tie holding a binder"></div>
  <div class="footer-space"></div>

  <svg class="promo-burst" viewBox="-140 -140 280 280" aria-hidden="true">
    <defs>
      <linearGradient id="burstFill" x1="0" y1="0" x2="0" y2="1">
        <stop offset="0" stop-color="#f7b3b6"/>
        <stop offset="0.3" stop-color="#e0454b"/>
        <stop offset="0.6" stop-color="#c0161d"/>
        <stop offset="1" stop-color="#8e0d12"/>
      </linearGradient>
    </defs>
    <polygon fill="url(#burstFill)" stroke="#e01c24" stroke-width="4" stroke-linejoin="miter"
      points="130,0 102.8,16.2 123.6,40.2 92.7,47.2 105.2,76.4 73.5,73.5 76.4,105.2 47.2,92.7 40.2,123.6 16.2,102.8 0,130 -16.2,102.8 -40.2,123.6 -47.2,92.7 -76.4,105.2 -73.5,73.5 -105.2,76.4 -92.7,47.2 -123.6,40.2 -102.8,16.2 -130,0 -102.8,-16.2 -123.6,-40.2 -92.7,-47.2 -105.2,-76.4 -73.5,-73.5 -76.4,-105.2 -47.2,-92.7 -40.2,-123.6 -16.2,-102.8 0,-130 16.2,-102.8 40.2,-123.6 47.2,-92.7 76.4,-105.2 73.5,-73.5 105.2,-76.4 92.7,-47.2 123.6,-40.2 102.8,-16.2"/>
  </svg>
  <div class="promo-text promo-title">REMOTE<br>SESSIONS</div>
  <div class="promo-rule" style="top:280px"></div>
  <div class="promo-text promo-course">12 SESSION COURSE</div>
  <div class="promo-rule" style="top:308px"></div>
  <div class="promo-text promo-start">CLASSES STARTING</div>
  <div class="promo-text promo-date">JUNE 16</div>
</main>
</body>
</html>
```